Velmora - 3D medical animations and high end visual content

Our company creates high end visual content and animations for medical global companies.
Our website - www.velmora-studio.example
We would like to have an amazing business card for our CEO that he can use in the following exhebitions he is going to attend.
It is very important that the design will be memorable and diffrent. It has to reflect our brand design (you can have it from our website)
We would like to transmit innovation, prestige, luxury, aesthetics.
The card has to be Double Sided

Target Market(s)

Marketing managers in medical global companys

Industry/Entity Type

It Company

Contact Information for Business Card

Requirements
Nice to have
• It is very important that the design will be memorable and diffrent. It has to reflect our brand design (you can have it from our website)

```html
<!DOCTYPE html>
<html lang="en">
<head>
<meta charset="utf-8">
<title>Velmora — Business Card</title>
<link href="https://fonts.googleapis.com/css2?family=Open+Sans:wght@400;600;700&display=swap" rel="stylesheet">
<style>
  :root {
    --page-bg: #e9e9e7;
    --card-black: #050505;
    --back-black: #161616;
    --teal: #1690a8;
    --white: #ffffff;
    --muted: #c9c9c9;
  }
  html, body {
    margin: 0;
    padding: 0;
    width: 1200px;
    height: 987px;
    overflow: hidden;
    background: var(--page-bg);
    font-family: "Open Sans", Arial, sans-serif;
  }
  .canvas {
    position: relative;
    width: 1200px;
    height: 987px;
  }
  .card {
    position: absolute;
    left: 293px;
    width: 615px;
    height: 352px;
    border-radius: 16px;
    overflow: hidden;
    box-shadow: 0 4px 12px rgba(0,0,0,0.25);
  }
  .card--front { top: 130px; background: var(--card-black); }
  .card--back  { top: 505px; background: var(--back-black); }

  .wordmark {
    position: absolute;
    font-weight: 400;
    color: var(--white);
    letter-spacing: 0.04em;
    line-height: 1;
    white-space: nowrap;
  }
  .card--front .wordmark {
    right: 53px;
    top: 52px;
    font-size: 37px;
  }
  .card--back .wordmark {
    left: 0;
    right: 0;
    top: 154px;
    text-align: center;
    font-size: 50px;
  }

  .holder-name {
    position: absolute;
    left: 35px;
    top: 170px;
    margin: 0;
    font-size: 21px;
    font-weight: 600;
    color: var(--teal);
    letter-spacing: 0.01em;
  }
  .holder-role {
    position: absolute;
    left: 35px;
    top: 201px;
    width: 527px;
    display: flex;
    align-items: center;
    gap: 6px;
    font-size: 15px;
    color: var(--white);
  }
  .holder-role::after {
    content: "";
    flex: 1;
    height: 1px;
    background: var(--white);
  }
  .contact-list {
    position: absolute;
    left: 37px;
    top: 233px;
    margin: 0;
    padding: 0;
    list-style: none;
  }
  .contact-list li {
    display: flex;
    align-items: center;
    height: 23.5px;
    font-size: 15px;
    color: var(--muted);
  }
  .contact-icon {
    width: 15px;
    height: 15px;
    margin-right: 8px;
    fill: var(--teal);
  }
  .bottom-band {
    position: absolute;
    left: 0;
    bottom: 0;
    width: 615px;
    height: 40px;
  }
  .website {
    position: absolute;
    right: 18px;
    bottom: 8px;
    font-size: 15.5px;
    color: var(--white);
    letter-spacing: 0.02em;
  }
  .back-pattern {
    position: absolute;
    inset: 0;
    background: linear-gradient(180deg, #1a1a1a, #111111);
  }
</style>
</head>
<body>
<main class="canvas">

  <section class="card card--front" aria-label="Business card front">
    <div class="wordmark">VELMORA</div>

    <h1 class="holder-name">ELAN MORADI</h1>
    <div class="holder-role">Founder&amp;CEO</div>

    <ul class="contact-list">
      <li>
        <svg class="contact-icon" viewBox="0 0 24 24" aria-hidden="true"><path d="M6.6 10.8a15.1 15.1 0 0 0 6.6 6.6l2.2-2.2c.3-.3.7-.4 1-.2 1.1.4 2.3.6 3.6.6.6 0 1 .4 1 1V20c0 .6-.4 1-1 1A17 17 0 0 1 3 4c0-.6.4-1 1-1h3.5c.6 0 1 .4 1 1 0 1.3.2 2.5.6 3.6.1.3 0 .7-.2 1z"/></svg>
        +972-70-5550147
      </li>
      <li>
        <svg class="contact-icon" viewBox="0 0 24 24" aria-hidden="true"><path d="M7 1h10a2 2 0 0 1 2 2v18a2 2 0 0 1-2 2H7a2 2 0 0 1-2-2V3a2 2 0 0 1 2-2zm0 3v14h10V4zm5 15.5a1 1 0 1 0 0 2 1 1 0 0 0 0-2z"/></svg>
        +972-50-5550283
      </li>
      <li>
        <svg class="contact-icon" viewBox="0 0 24 24" aria-hidden="true"><path d="M2 5h20v14H2zm2 2v.5l8 5 8-5V7zm0 2.8V17h16V9.8l-8 5z"/></svg>
        elan@velmora-studio.example
      </li>
    </ul>

    <svg class="bottom-band" viewBox="0 0 615 40" aria-hidden="true">
      <path d="M0 30 H345 V40 H0 Z" fill="var(--teal)"/>
      <path d="M0 16 H345 Q350 16 354 13 L360 8 Q356 27 340 28 H0 Z" fill="var(--white)"/>
      <path d="M335 40 Q350 40 356 26 Q362 8 378 8 H615 V40 Z" fill="var(--teal)"/>
    </svg>
    <div class="website">www.velmora-studio.example</div>
  </section>

  <section class="card card--back" aria-label="Business card back">
    <div class="back-pattern" role="img" aria-label="Subtle dark repeating brand pattern"></div>
    <div class="wordmark">VELMORA</div>
  </section>

</main>
</body>
</html>
```